LumoPledge Crowdfunding Website 1st Page

I am looking to have a first page created for a new crowd funding website that knocks down the biggest hurdle that creative types and start ups face, legal costs. For creative projects and innovative products, we are providing intellectual property and certain other legal services wrapped into the project costs.

I am using a white label crowdfunding platform that that has a standard look and feel of most crowdfunding sites e.g. tiles with campaigns, listing of campaigns categories, create new campaign options, and donate to campaigns etc. The white label program is branded with the LumoPledge logo and colors. At present there is a front page that is just a place holder for someone at ArtHively's great design! What I need is an eye-catching first page that visually and through content optimizes the LumoPledge brand. (There should be space for content for those looking to raise money and those looking to donate to campaigns.)

www.fundvexora.com is, of course, the reigning King of crowdfunding. They have been so successful that they no longer have to entice people to launch campaigns there. (So they don't speak as much to those looking to raise money.) Unlike Fundvexora, of the challenges is that I have two customers I need to engage. The first is the potential crowdfund campaign owner who is looking to raise money. The second customer is the donor.

I am looking for a smart page from a marketing standpoint that also grabs you. One should feel the energy of "the crowd" when they look at the page.

Some information regarding the logo: The font is Kabel BK BT. The primary blue is R33, G121, B 159. Hex21799F and the primary greenis R179, G210, B54 Hex B3D236. The third file is a slight variation on the LP logo that you are free to use as well. (Unfortunately, I don't have all the color information for that one readily available.) If you need more files, please just let me know.

Industry/Entity Type

Marketing

Font styles to use
Other font styles liked:
• Kabel Bk BT or complimentary

Requirements
Must have
• Please use the slogan "Where the crowd meets great ideas".

```html
<!DOCTYPE html>
<html lang="en">
<head>
<meta charset="utf-8">
<title>LumoPledge – Where the crowd meets great ideas</title>
<link rel="stylesheet" href="https://fonts.googleapis.com/css2?family=Oswald:wght@400;500&family=Open+Sans:wght@400;600;700&family=Lora:ital@1&display=swap">
<style>
:root{
  --blue:#21799f;
  --green:#a9c61f;
  --orange:#e1532b;
  --red:#d63a3c;
  --slate:#35404c;
  --panel:#eeeeea;
  --ink:#3a3a3a;
  --muted:#8c8c8c;
  --yellow:#f2d21a;
  --white:#ffffff;
}
*{box-sizing:border-box;margin:0;padding:0}
html,body{width:1200px;height:2857px;overflow:hidden}
body{position:relative;background:var(--white);font-family:"Open Sans",Arial,sans-serif;color:var(--ink)}
.abs{position:absolute}
.rainbow{position:absolute;left:0;width:1200px;height:7px;
  background:linear-gradient(90deg,#e1532b 0 14%,#f2a31a 14% 28%,#f2d21a 28% 42%,#a9c61f 42% 57%,#21799f 57% 71%,#3a5fbf 71% 85%,#8b4aa8 85% 100%)}
.btn{display:inline-block;color:var(--white);font-weight:600;text-transform:uppercase;text-align:center;white-space:nowrap}
.btn-green{background:var(--green)}
.btn-orange{background:var(--orange)}

/* header */
.logo{left:104px;top:34px;display:flex;align-items:center;gap:12px}
.logo-dot{width:62px;height:62px;border-radius:50%;background:var(--blue)}
.logo-name{font-size:40px;font-weight:600;color:var(--blue);letter-spacing:-0.5px;margin-top:40px}
.nav{font-size:17px;font-weight:600;color:#333;line-height:34px}
.nav-col1{left:521px;top:30px}
.nav-col2{left:719px;top:30px}
.nav-divider{left:679px;top:30px;width:1px;height:100px;background:#999}
.header-cta{left:960px;top:38px;width:135px;height:33px;line-height:33px;font-size:13px}
.account{top:102px;font-size:16px;font-weight:600;color:#333;display:flex;align-items:center;gap:8px}
.account-sep{left:970px;top:98px;width:1px;height:30px;background:#999}

/* hero */
.hero{left:0;top:157px;width:1200px;height:533px;
  background:radial-gradient(circle at 78% 30%,#f2c9a4 0,#d69a6a 18%,transparent 40%),
             radial-gradient(circle at 20% 60%,#e6b48e 0,#b87a55 20%,transparent 45%),
             linear-gradient(120deg,#6aa7cf 0%,#c9d7e0 35%,#e9c24a 55%,#d85a5a 75%,#3c7fb5 100%)}
.hero-box{left:71px;top:281px;width:655px;height:333px;background:rgba(40,46,56,.86);border-top:7px solid var(--blue);padding:38px 40px 0 50px;color:var(--white)}
.hero-title{font-family:"Oswald",Impact,sans-serif;font-weight:400;font-size:37px;line-height:50px;text-transform:uppercase;letter-spacing:0}
.hero-stats{margin-top:56px;display:flex;justify-content:space-between;font-family:"Lora",Georgia,serif;font-style:italic;font-size:18px}
.progress{height:8px;background:var(--white);margin-top:6px}
.progress span{display:block;height:100%;background:var(--yellow)}
.hero-actions{margin-top:30px;display:flex;align-items:center;gap:10px;font-size:13px}
.hero-actions .btn{height:30px;line-height:30px;padding:0 12px;font-size:12px}

/* content panel */
.panel{left:105px;top:690px;width:990px;height:1358px;background:var(--panel)}
.section-bar{left:124px;width:950px;height:29px;display:flex;align-items:center;gap:12px}
.tag{height:29px;line-height:29px;padding:0 12px;font-size:12px;font-weight:700;color:var(--white);text-transform:uppercase}
.tag-dark{background:var(--slate)}
.tag-orange{background:var(--orange)}
.arrows{margin-left:auto;display:flex;gap:12px}
.arrow{width:29px;height:29px;border-radius:50%;background:var(--white);display:flex;align-items:center;justify-content:center}
.cards{left:124px;width:950px;display:flex;gap:17px}
.card{width:226px;background:var(--white);position:relative}
.card-img{height:147px}
.cause-card{height:564px}
.cause-title{padding:24px 16px 0;font-size:19px;font-weight:400;line-height:29px;text-align:center;color:#444}
.cause-text{padding:14px 16px 0;font-size:12.5px;line-height:24px;text-align:center;color:var(--red)}
.cause-foot{position:absolute;left:0;bottom:0;width:226px;height:148px;background:var(--slate);padding:22px 20px 0;color:var(--white);text-align:center;font-family:"Lora",Georgia,serif;font-style:italic;font-size:14px;line-height:19px}
.cause-foot::before{content:"";position:absolute;left:103px;top:-12px;border:10px solid transparent;border-top:0;border-bottom:12px solid var(--slate)}
.cause-foot .progress{height:6px;margin:8px 0 0}
.card-actions{display:flex;justify-content:space-between;margin-top:24px}
.card-actions .btn{font-family:"Open Sans",Arial,sans-serif;font-style:normal;height:24px;line-height:24px;font-size:9px;padding:0 7px}
.news-card{height:567px;text-align:center}
.news-img{height:98px}
.news-title{padding:16px 14px 0;height:150px;font-size:19px;font-weight:400;line-height:30px;color:#333}
.news-date{font-family:"Lora",Georgia,serif;font-size:14px;color:#555;padding:8px 0 20px;border-bottom:1px solid #e3e3e3;margin:0 28px}
.news-text{padding:16px 30px 0;height:226px;font-size:12px;line-height:22px;color:var(--muted)}
.news-card .btn{font-size:9px;height:25px;line-height:25px;padding:0 9px}

/* crowd band */
.crowd{left:0;top:2048px;width:1200px;height:409px;
  background:linear-gradient(135deg,#3b4552 0%,#4a5563 40%,#3d4855 70%,#343e4a 100%)}
.crowd-quote{left:0;top:2140px;width:1200px;text-align:center;color:var(--white);font-size:40px;font-weight:400}
.crowd-text{left:0;top:2218px;width:1200px;text-align:center;color:var(--white);font-size:15px;line-height:36px}
.crowd-cta{left:500px;top:2333px;width:205px;height:50px;line-height:50px;font-size:14px;border-radius:4px}

/* footer */
.footer{left:0;top:2457px;width:1200px;height:400px;background:var(--slate)}
.footer-head{top:2510px;font-size:21px;font-weight:700;color:var(--white)}
.footer-text{left:133px;top:2553px;width:280px;font-size:12px;line-height:25px;color:#9aa4ad}
.snap-grid{left:493px;top:2560px;width:205px;height:207px;background:linear-gradient(135deg,#7c8690,#b9a58c 35%,#5d7086 65%,#a6b2bd)}
.social{left:800px;top:2562px;display:flex;gap:8px}
.social span{width:26px;height:26px;border-radius:50%;background:#8d969f}
.news-head{left:800px;top:2612px;font-size:19px;font-weight:700;color:var(--white)}
.news-sub{left:800px;top:2639px;font-size:13px;font-weight:700;color:var(--white)}
.news-input{left:800px;top:2660px;width:267px;height:30px;background:var(--white)}
.news-btn{left:800px;top:2700px;width:117px;height:29px;line-height:29px;font-size:13px;text-transform:none}
.copyright{left:105px;top:2806px;font-size:13px;font-weight:600;color:var(--white)}
</style>
</head>
<body>

<div class="rainbow" style="top:0"></div>

<header>
  <div class="abs logo"><span class="logo-dot"></span><span class="logo-name">LumoPledge</span></div>
  <nav>
    <div class="abs nav nav-col1">HOME<br>OUR CAUSES<br>RECENT NEWS</div>
    <div class="abs nav-divider"></div>
    <div class="abs nav nav-col2">EVENTS<br>DONATE<br>CONTACT US</div>
  </nav>
  <a class="abs btn btn-green header-cta">Make a Donation</a>
  <div class="abs account" style="left:874px">
    <svg width="16" height="18" viewBox="0 0 16 18"><rect x="1" y="8" width="14" height="10" fill="#333"/><path d="M4 8V5a4 4 0 0 1 8 0v3" fill="none" stroke="#333" stroke-width="2.4"/></svg>SIGN IN</div>
  <div class="abs account-sep"></div>
  <div class="abs account" style="left:990px">
    <svg width="16" height="18" viewBox="0 0 16 18"><circle cx="8" cy="5" r="4.5" fill="#333"/><path d="M0 18a8 7 0 0 1 16 0z" fill="#333"/></svg>REGISTER</div>
</header>

<section>
  <div class="abs hero" role="img" aria-label="Photo of smiling children in a circle looking down at the camera"></div>
  <div class="abs hero-box">
    <h1 class="hero-title">Conference : Save for your child's<br>education</h1>
    <div class="hero-stats"><span>$7186 Donated</span><span>89.83% Funded</span></div>
    <div class="progress"><span style="width:89.8%"></span></div>
    <div class="hero-actions"><a class="btn btn-orange">More Details</a><span>or</span><a class="btn btn-green">Make a Donation</a></div>
  </div>
</section>

<main>
  <div class="abs panel"></div>

  <div class="abs section-bar" style="top:729px">
    <span class="tag tag-dark">Causes</span><span class="tag tag-orange">View All</span>
    <div class="arrows">
      <span class="arrow"><svg width="8" height="10"><path d="M6 1 2 5l4 4" fill="none" stroke="#555" stroke-width="1.5"/></svg></span>
      <span class="arrow"><svg width="8" height="10"><path d="M2 1l4 4-4 4" fill="none" stroke="#555" stroke-width="1.5"/></svg></span>
    </div>
  </div>

  <div class="abs cards" style="top:786px">
    <article class="card cause-card">
      <div class="card-img" role="img" aria-label="Photo of two smiling children" style="background:linear-gradient(135deg,#8a5a3c,#c99a72 50%,#5a3a2a)"></div>
      <h3 class="cause-title">Child, Youth and Family Services</h3>
      <p class="cause-text">Vivamus adipiscing bibendum neque, vitae vulputate justo ultricies ac. Pellentesque nec tempor nunc, at condimentum lacus.</p>
      <div class="cause-foot">$42734 Donated<br>50.6% Funded<div class="progress"><span style="width:50.6%"></span></div>
        <div class="card-actions"><a class="btn btn-orange">More Details</a><a class="btn btn-green">Make a Donation</a></div></div>
    </article>
    <article class="card cause-card">
      <div class="card-img" role="img" aria-label="Underwater photo of a sea turtle over a coral reef" style="background:linear-gradient(180deg,#1d7fc0,#3aa2d6 55%,#c65b3a)"></div>
      <h3 class="cause-title">Sea Turtles – Office of Ocean Wildcare</h3>
      <p class="cause-text">Quisque sem tellus, elementum at malesuada sed, vulputate at orci. Suspendisse vitae fringilla sem. Suspendisse sodales scelerisque.</p>
      <div class="cause-foot">$13827 Donated<br>72.3% Funded<div class="progress"><span style="width:72.3%"></span></div>
        <div class="card-actions"><a class="btn btn-orange">More Details</a><a class="btn btn-green">Make a Donation</a></div></div>
    </article>
    <article class="card cause-card">
      <div class="card-img" role="img" aria-label="Photo of a group of adults seated in a training session" style="background:linear-gradient(135deg,#c9cfd6,#7d8a99 50%,#4a5566)"></div>
      <h3 class="cause-title">T.C. Training and Education Savings Grant</h3>
      <p class="cause-text">Quisque sem tellus, elementum at malesuada sed, vulputate at orci. Suspendisse vitae fringilla sem. Suspendisse sodales scelerisque.</p>
      <div class="cause-foot">$32115 Donated<br>83.1% Funded<div class="progress"><span style="width:83.1%"></span></div>
        <div class="card-actions"><a class="btn btn-orange">More Details</a><a class="btn btn-green">Make a Donation</a></div></div>
    </article>
    <article class="card cause-card">
      <div class="card-img" role="img" aria-label="Photo of a tree frog on a leaf" style="background:linear-gradient(135deg,#1e4a1c,#5fa32e 50%,#2a5c22)"></div>
      <h3 class="cause-title">Save the Amazon Rainforest Organisation</h3>
      <p class="cause-text">Quisque sem tellus, elementum at malesuada sed, vulputate at orci. Suspendisse vitae fringilla sem. Suspendisse sodales scelerisque.</p>
      <div class="cause-foot">$23669 Donated<br>96.9% Funded<div class="progress"><span style="width:96.9%"></span></div>
        <div class="card-actions"><a class="btn btn-orange">More Details</a><a class="btn btn-green">Make a Donation</a></div></div>
    </article>
  </div>

  <div class="abs section-bar" style="top:1390px">
    <span class="tag tag-dark">News</span><span class="tag tag-orange">View All</span>
    <div class="arrows">
      <span class="arrow"><svg width="8" height="10"><path d="M6 1 2 5l4 4" fill="none" stroke="#555" stroke-width="1.5"/></svg></span>
      <span class="arrow"><svg width="8" height="10"><path d="M2 1l4 4-4 4" fill="none" stroke="#555" stroke-width="1.5"/></svg></span>
    </div>
  </div>

  <div class="abs cards" style="top:1445px">
    <article class="card news-card">
      <div class="news-img" role="img" aria-label="Photo of a red panda resting on a log" style="background:linear-gradient(135deg,#3a3a32,#a8522a 50%,#6b6a58)"></div>
      <h3 class="news-title">Missing red panda from Maplewood Zoo found in Town</h3>
      <p class="news-date">June 27, 2013</p>
      <p class="news-text">Sed a interdum ante. Integer vel libero viverra, venenatis nisi facilisis, fringilla arcu. Curabitur a diam sit amet sapien rhoncus aliquet a eget ligula.</p>
      <a class="btn btn-orange">Continue Reading</a>
    </article>
    <article class="card news-card">
      <div class="news-img" role="img" aria-label="Illustration of a hand with app icons on a blue background" style="background:linear-gradient(135deg,#0d3f8a,#2f7fd0 50%,#0a2f6a)"></div>
      <h3 class="news-title">Tale Of A Top-10 App, Part 2: Marketing And Launch</h3>
      <p class="news-date">July 15, 2013</p>
      <p class="news-text">Sed a interdum ante. Integer vel libero viverra, venenatis nisi facilisis, fringilla arcu. Curabitur a diam sit amet sapien rhoncus aliquet a eget ligula.</p>
      <a class="btn btn-orange">Continue Reading</a>
    </article>
    <article class="card news-card">
      <div class="news-img" role="img" aria-label="Illustration of a head silhouette filled with colourful notes" style="background:linear-gradient(135deg,#2c6a66,#5a9a8e 50%,#e2b64a)"></div>
      <h3 class="news-title">The Joy Of Illustrated Maps In The Era Of GeoSphere Maps</h3>
      <p class="news-date">July 15, 2013</p>
      <p class="news-text">Sed a interdum ante. Integer vel libero viverra, venenatis nisi facilisis, fringilla arcu. Curabitur a diam sit amet sapien rhoncus aliquet a eget ligula.</p>
      <a class="btn btn-orange">Continue Reading</a>
    </article>
    <article class="card news-card">
      <div class="news-img" role="img" aria-label="Photo of students sitting on grass at a summer camp" style="background:linear-gradient(180deg,#dfe8d6,#8bb06a 55%,#4e7a3a)"></div>
      <h3 class="news-title">Summer Language Camp in English or French</h3>
      <p class="news-date">June 27, 2013</p>
      <p class="news-text">Sed a interdum ante. Integer vel libero viverra, venenatis nisi facilisis, fringilla arcu. Curabitur a diam sit amet sapien rhoncus aliquet a eget ligula.</p>
      <a class="btn btn-orange">Continue Reading</a>
    </article>
  </div>
</main>

<section>
  <div class="abs crowd" role="img" aria-label="Dimmed mosaic of many small crowd portrait photos"></div>
  <h2 class="abs crowd-quote" style="font-weight:400">"Where the crowd meets great ideas"</h2>
  <p class="abs crowd-text">Etiam molestie, quam eget dignissim dapibus, diam libero auctor justo, a eleifend<br>urna tellus et ligula. Curabitur elementum diam nec lacus pretium.</p>
  <a class="abs btn btn-green crowd-cta">Make a Donation Now</a>
</section>

<footer>
  <div class="abs footer"></div>
  <h4 class="abs footer-head" style="left:133px">Powerful Foundation</h4>
  <p class="abs footer-text">Etiam molestie, quam eget dignissim dapibus, diam libero auctor justo, a eleifend urna tellus et ligula. Curabitur elementum diam nec. Aliquam dictum feugiat mi sed varius. Nulla ultrices a neque ac commodo. Donec quis pellentesque arcu. Duis id pulvinar sapien. Nam vel nisl vel mauris feugiat porta.</p>
  <h4 class="abs footer-head" style="left:493px">From Snapwell</h4>
  <div class="abs snap-grid" role="img" aria-label="Grid of sixteen small community photos"></div>
  <h4 class="abs footer-head" style="left:800px">Follow Us</h4>
  <div class="abs social"><span></span><span></span><span></span><span></span><span></span></div>
  <h4 class="abs news-head">Newsletter</h4>
  <p class="abs news-sub">Sign Up for Our Newsletter</p>
  <div class="abs news-input"></div>
  <a class="abs btn btn-orange news-btn">Subscribe</a>
  <p class="abs copyright">Copyright © 2013 lumopledge. All rights reserved.</p>
  <div class="rainbow" style="top:2850px"></div>
</footer>

</body>
</html>
```